Website for QuillbrookCrew presentation

We need a new website, ideally as a wordpress there, for QuillbrookCrew - we focus on machine learning, big data, data science and data analytics. This website should have two main sections - team presentation, introduction and offered services as static pages, and a blog section.

Target Market(s)

Companies which would like to hire the consultants for data science

Industry/Entity Type

Data Service

Font styles to use
Sans Serif

Colors

Designer to choose colors to be used in the design.

Requirements
Must have
• Wordpress template, blog and presentation pages, nice background images, incorporate the existing logo from brief
Nice to have
• match the word and ppt existing templates for quillbrook crew

```html
<!DOCTYPE html>
<html lang="en">
<head>
<meta charset="utf-8">
<title>QuillbrookCrew</title>
<link rel="stylesheet" href="https://fonts.googleapis.com/css2?family=Lato:wght@400;700;900&family=Open+Sans:wght@400;600&display=swap">
<style>
:root{
  --blue:#1b75bb;
  --blue-dark:#135c95;
  --ink:#111418;
  --text:#555b63;
  --muted:#8a9098;
  --line:#e3e6ea;
  --pale:#f4f5f7;
  --ghost:#e6e8eb;
  --footer:#262626;
  --white:#ffffff;
}
*{margin:0;padding:0;box-sizing:border-box}
html,body{width:1200px;height:2880px;overflow:hidden}
body{position:relative;background:var(--white);font-family:"Open Sans",Arial,sans-serif;color:var(--text)}
.abs{position:absolute}

/* header */
.site-header{left:0;top:0;width:1200px;height:126px;border-top:4px solid var(--blue);background:var(--white)}
.brand{left:100px;top:34px;display:flex;align-items:center;gap:12px}
.brand-dot{width:40px;height:40px;border-radius:50%;background:var(--blue)}
.brand-name{font-family:Lato,sans-serif;font-weight:900;font-size:24px;line-height:26px;color:var(--blue);width:140px}
.contact-bar{right:100px;top:30px;display:flex;gap:22px;font-size:14px;color:#555;align-items:center}
.contact-bar span{display:flex;align-items:center;gap:8px}
.contact-bar .sep{width:1px;height:14px;background:#999}
.main-nav{right:96px;top:76px;display:flex;gap:30px;font-family:Lato,sans-serif;font-weight:700;font-size:15px;color:#222;align-items:center}
.main-nav .active{color:var(--blue);position:relative}
.main-nav .active::before{content:"";position:absolute;left:12px;top:-22px;width:12px;height:12px;background:radial-gradient(circle at 3px 3px,var(--blue) 2.5px,transparent 3px),radial-gradient(circle at 9px 6px,var(--blue) 2.5px,transparent 3px),radial-gradient(circle at 5px 10px,var(--blue) 2px,transparent 2.5px)}

/* hero */
.hero{left:0;top:126px;width:1200px;height:557px;background:radial-gradient(ellipse at 58% 42%,#1f6fd6 0%,#0c2f7a 35%,#050b1e 70%,#02040b 100%)}
.hero-title{left:0;top:370px;width:1200px;text-align:center;font-family:Lato,sans-serif;font-weight:900;font-size:52px;color:var(--white);letter-spacing:.5px;text-shadow:0 2px 8px rgba(0,0,0,.5)}

/* side labels */
.side-label{left:20px;width:40px;display:flex;flex-direction:column;align-items:center;gap:50px}
.side-label b{writing-mode:vertical-rl;transform:rotate(180deg);font-family:Lato,sans-serif;font-weight:900;font-size:20px;letter-spacing:4px;color:var(--ink)}
.side-label i{display:block;width:3px;height:12px;background:var(--blue)}
.ghost{font-family:Lato,sans-serif;font-weight:900;color:var(--ghost);white-space:nowrap}

/* about */
.about{left:0;top:683px;width:1200px;height:472px;background:linear-gradient(#fafbfc,#ffffff)}
.about-visual{left:96px;top:103px;width:437px;height:252px;border:4px solid var(--white);box-shadow:0 3px 12px rgba(0,0,0,.2);background:linear-gradient(135deg,#5d7a9c,#2f4a6c 55%,#1a2c48)}
.about-title{left:596px;top:92px;font-family:Lato,sans-serif;font-weight:900;font-size:30px;color:var(--ink)}
.about-copy{left:596px;top:156px;width:506px;font-size:12.5px;line-height:24px;color:#666}
.btn{display:inline-flex;align-items:center;justify-content:center;gap:6px;background:var(--blue);color:var(--white);font-family:Lato,sans-serif;font-weight:900;font-size:14px;border-radius:24px}
.about .btn{position:absolute;left:596px;top:310px;width:157px;height:44px}
.about .ghost{right:8px;top:60px;font-size:76px;writing-mode:vertical-rl}

/* team */
.team{left:0;top:1155px;width:1200px;height:640px;background:var(--pale)}
.team .ghost{left:0;width:1200px;text-align:center;top:68px;font-size:70px;color:#e0e2e5}
.section-title{font-family:Lato,sans-serif;font-weight:900;font-size:30px;color:var(--ink)}
.team .section-title{left:0;width:1200px;top:88px;text-align:center}
.team-sub{left:0;width:1200px;top:146px;text-align:center;font-size:12.5px;color:#555}
.member{width:486px;height:180px;display:flex;align-items:flex-start;gap:34px;padding:22px 20px}
.member.is-featured{background:var(--white);box-shadow:0 2px 14px rgba(0,0,0,.14)}
.portrait{flex:none;width:132px;height:132px;border-radius:50%;border:3px solid #333;box-shadow:0 0 0 4px var(--white) inset}
.is-featured .portrait{border-color:var(--blue)}
.member-name{font-family:Lato,sans-serif;font-weight:700;font-size:19px;color:var(--ink);margin-top:6px}
.member-role{font-family:Lato,sans-serif;font-weight:700;font-size:15px;color:var(--blue);margin-top:10px}
.member-bio{font-size:12.5px;line-height:23px;color:#666;margin-top:12px;width:280px}

/* blog */
.blog{left:0;top:1795px;width:1200px;height:730px;background:var(--white)}
.blog .ghost{right:100px;top:50px;font-size:66px;color:#e4e6e9}
.blog .section-title{left:132px;top:86px}
.blog-intro{left:132px;top:148px;width:940px;font-size:12.5px;line-height:24px;color:#555}
.post-list{left:132px;top:230px;width:940px;border-top:1px solid var(--line)}
.post{display:flex;height:78px;border-bottom:1px solid var(--line);align-items:center}
.post-date{width:210px;padding-left:28px;display:flex;align-items:center;gap:8px;font-size:13.5px;color:#333;border-right:1px solid var(--line);height:54px}
.post-title{padding-left:42px;font-weight:600;font-size:17.5px;color:var(--ink)}

/* footer */
.site-footer{left:0;top:2525px;width:1200px;height:355px}
.footer-photo{left:0;top:0;width:400px;height:355px;background:linear-gradient(160deg,#cfe3f5 0%,#6f9fcc 35%,#1d4f8a 70%,#0e2c55 100%)}
.footer-main{left:400px;top:0;width:400px;height:355px;background:var(--footer);color:var(--white);text-align:center}
.footer-map{left:800px;top:0;width:400px;height:355px;background:linear-gradient(135deg,#eeebe3,#e4e1d8)}
.to-top{left:574px;top:-26px;width:52px;height:52px;border-radius:50%;background:var(--white);display:flex;align-items:center;justify-content:center;box-shadow:0 1px 6px rgba(0,0,0,.2)}
.footer-head{font-family:Lato,sans-serif;font-weight:700;font-size:15.5px;letter-spacing:.3px}
.email-field{margin:20px auto 0;width:282px;height:40px;border:1px solid #bbb;text-align:left;font-size:12px;padding:11px 14px}
.footer-main .btn{width:130px;height:38px;margin-top:16px;font-size:14px}
.footer-line{font-size:12.5px;display:flex;justify-content:center;align-items:center;gap:12px;margin-top:12px}
.copyright{font-size:12.5px;margin-top:24px}
.direction-btn{left:818px;top:18px;background:var(--white);height:34px;padding:0 14px;display:flex;align-items:center;gap:7px;font-family:Lato,sans-serif;font-weight:700;font-size:12px;color:#333;box-shadow:0 1px 3px rgba(0,0,0,.25)}
</style>
</head>
<body>

<header class="site-header abs">
  <div class="brand abs"><span class="brand-dot"></span><span class="brand-name">QUILLBROOK CREW</span></div>
  <div class="contact-bar abs">
    <span><svg width="14" height="14" viewBox="0 0 24 24"><path fill="#1b75bb" d="M6.6 10.8a15 15 0 0 0 6.6 6.6l2.2-2.2a1 1 0 0 1 1-.25 11.4 11.4 0 0 0 3.6.57 1 1 0 0 1 1 1V20a1 1 0 0 1-1 1A17 17 0 0 1 3 4a1 1 0 0 1 1-1h3.5a1 1 0 0 1 1 1c0 1.25.2 2.45.57 3.6a1 1 0 0 1-.25 1z"/></svg>(+1) 555 014 2290</span>
    <i class="sep"></i>
    <span><svg width="15" height="12" viewBox="0 0 20 16"><path fill="#1b75bb" d="M0 1h20v14H0zM1.5 2.5 10 9l8.5-6.5"/><path fill="none" stroke="#fff" stroke-width="1.5" d="M1 2l9 7 9-7"/></svg>office@quillbrookcrew.com</span>
  </div>
  <nav class="main-nav abs">
    <span class="active">HOME</span><span>ABOUT US</span><span>OUR SERVICES</span><span>BLOG</span><span>TEAM</span><span>CONTACT US</span>
    <svg width="15" height="15" viewBox="0 0 20 20"><circle cx="8" cy="8" r="6" fill="none" stroke="#222" stroke-width="2.5"/><path d="M12.5 12.5 18 18" stroke="#222" stroke-width="3"/></svg>
  </nav>
</header>

<section class="hero abs" role="img" aria-label="Glowing blue circuit-board brain on a dark background with binary digits"></section>
<h1 class="hero-title abs">QUILLBROOK CREW</h1>

<section class="about abs">
  <div class="side-label abs" style="top:130px"><b>ABOUT US</b><i></i></div>
  <div class="ghost abs">ABOUT US</div>
  <div class="about-visual abs" role="img" aria-label="Businessman touching a hexagon diagram of machine learning, statistics and artificial intelligence"></div>
  <h2 class="about-title abs">WELCOME TO QUILLBROOK CREW</h2>
  <p class="about-copy abs">At vero eos et accusamus et iusto odio dignissimos ducimus qui blanditiis praesentium voluptatum deleniti atque corrupti quos dolores et quas molestias excepturi sint occaecati cupiditate non provident, similique sunt in culpa qui officia deserunt mollitia animi, id est laborum et dolorum fuga. Et harum quidem rerum facilis est et expedita distinctio. Nam libero tempore, cum soluta nobis est eligendi optio cumque</p>
  <span class="btn">READ MORE <svg width="13" height="13" viewBox="0 0 16 16"><circle cx="8" cy="8" r="8" fill="#fff"/><path d="M6 4.5 9.5 8 6 11.5" fill="none" stroke="#1b75bb" stroke-width="2"/></svg></span>
</section>

<section class="team abs">
  <div class="side-label abs" style="top:220px"><b>OUR TEAM</b><i></i></div>
  <div class="ghost abs">OUR TEAM</div>
  <h2 class="section-title abs">OUR TEAM</h2>
  <p class="team-sub abs">We understand the success secrets of the world's most successful business teams.</p>

  <article class="member abs" style="left:100px;top:190px">
    <div class="portrait" role="img" aria-label="Portrait of the founder" style="background:linear-gradient(#e8e8e8,#9aa3ad)"></div>
    <div><div class="member-name">MARLO FINCH</div><div class="member-role">Founder &amp; CEO</div><p class="member-bio">Nemo enim ipsam voluptem quia voluptas sit aspernatur aut odit aut fugit sed quia</p></div>
  </article>
  <article class="member abs" style="left:617px;top:190px">
    <div class="portrait" role="img" aria-label="Portrait of the creative manager" style="background:linear-gradient(#f0f0f0,#8e959d)"></div>
    <div><div class="member-name">TAVIN REYES</div><div class="member-role">Creative Manager</div><p class="member-bio">Nemo enim ipsam voluptem quia voluptas sit aspernatur aut odit aut fugit sed quia</p></div>
  </article>
  <article class="member is-featured abs" style="left:100px;top:365px">
    <div class="portrait" role="img" aria-label="Portrait of the general manager" style="background:linear-gradient(#e9eef3,#9fb6cc)"></div>
    <div><div class="member-name">ELSA WREN</div><div class="member-role">General Manager</div><p class="member-bio">Nemo enim ipsam voluptem quia voluptas sit aspernatur aut odit aut fugit sed quia</p></div>
  </article>
  <article class="member abs" style="left:617px;top:365px">
    <div class="portrait" role="img" aria-label="Portrait of the administrative lead" style="background:linear-gradient(#f2f2f2,#7f868e)"></div>
    <div><div class="member-name">OREN PIKE</div><div class="member-role">Adminstrative Team</div><p class="member-bio">Nemo enim ipsam voluptem quia voluptas sit aspernatur aut odit aut fugit sed quia</p></div>
  </article>
</section>

<section class="blog abs">
  <div class="side-label abs" style="top:240px"><b>BLOG POST</b><i></i></div>
  <div class="ghost abs">BLOG POST</div>
  <h2 class="section-title abs">BLOG POST</h2>
  <p class="blog-intro abs">Nam libero tempore, cum soluta nobis est eligendi optio cumque nihil impedit quo minus id quod maxime placeat facere possimus, omnis voluptas tsdsb assumenda est, omnis dolor repellendus. Temporibus autem quibusdam et aut officiis debitis aut rerum necessitatibus saepe eveniet</p>
  <div class="post-list abs">
    <div class="post"><span class="post-date"><svg width="12" height="12" viewBox="0 0 12 12"><rect x="0.5" y="1.5" width="11" height="10" fill="none" stroke="#555"/><rect x="0.5" y="1.5" width="11" height="3" fill="#555"/></svg>June 08, 2018</span><span class="post-title">Nam libero tempore, cum soluta nobis est eligendi optio cumque nihil impedit.</span></div>
    <div class="post"><span class="post-date"><svg width="12" height="12" viewBox="0 0 12 12"><rect x="0.5" y="1.5" width="11" height="10" fill="none" stroke="#555"/><rect x="0.5" y="1.5" width="11" height="3" fill="#555"/></svg>June 15, 2018</span><span class="post-title">When our power of choice is untrammelled and when nothing prevents our being.</span></div>
    <div class="post"><span class="post-date"><svg width="12" height="12" viewBox="0 0 12 12"><rect x="0.5" y="1.5" width="11" height="10" fill="none" stroke="#555"/><rect x="0.5" y="1.5" width="11" height="3" fill="#555"/></svg>June 18, 2018</span><span class="post-title">I must explain to you how all this mistaken idea of denouncing pleasure praising.</span></div>
    <div class="post"><span class="post-date"><svg width="12" height="12" viewBox="0 0 12 12"><rect x="0.5" y="1.5" width="11" height="10" fill="none" stroke="#555"/><rect x="0.5" y="1.5" width="11" height="3" fill="#555"/></svg>June 22, 2018</span><span class="post-title">Quis autem vel eum iure reprehenderit qui in ea voluptate velit esse.</span></div>
    <div class="post"><span class="post-date"><svg width="12" height="12" viewBox="0 0 12 12"><rect x="0.5" y="1.5" width="11" height="10" fill="none" stroke="#555"/><rect x="0.5" y="1.5" width="11" height="3" fill="#555"/></svg>June 30, 2018</span><span class="post-title">Excepteur sint occaecat cupidatat non proident, sunt in culpa qui officia id est.</span></div>
  </div>
</section>

<footer class="site-footer abs">
  <div class="footer-photo abs" role="img" aria-label="Modern glass office tower against a blue sky"></div>
  <div class="footer-main abs">
    <div style="padding-top:52px">
      <div class="footer-head">NEWSLETTER SUBSCRIPTION</div>
      <div class="email-field">Email</div>
      <span class="btn">SUBCRIBE</span>
      <div class="footer-head" style="margin-top:26px">CONTACT US</div>
      <div class="footer-line"><svg width="13" height="13" viewBox="0 0 24 24"><path fill="#fff" d="M6.6 10.8a15 15 0 0 0 6.6 6.6l2.2-2.2a1 1 0 0 1 1-.25 11.4 11.4 0 0 0 3.6.57 1 1 0 0 1 1 1V20a1 1 0 0 1-1 1A17 17 0 0 1 3 4a1 1 0 0 1 1-1h3.5a1 1 0 0 1 1 1c0 1.25.2 2.45.57 3.6a1 1 0 0 1-.25 1z"/></svg>(+1) 555 014 2290</div>
      <div class="footer-line"><svg width="14" height="11" viewBox="0 0 20 16"><path fill="#fff" d="M0 1h20v14H0z"/><path fill="none" stroke="#262626" stroke-width="1.5" d="M1 2l9 7 9-7"/></svg>info@quillbrookcrew.com</div>
      <p class="copyright">© Copyright 2018 QuillbrookCrew. All Rights Reserved.</p>
    </div>
  </div>
  <div class="footer-map abs" role="img" aria-label="Road map of the office area with a red location pin"></div>
  <div class="direction-btn abs"><svg width="13" height="11" viewBox="0 0 14 12"><path fill="#333" d="M14 5 9 0v3C4 3 1 6 0 11c2-3 5-4 9-4v3z"/></svg>GET DIRECTION</div>
  <div class="to-top abs"><svg width="20" height="20" viewBox="0 0 20 20"><path d="M4 10 10 4l6 6M4 16l6-6 6 6" fill="none" stroke="#222" stroke-width="2.2"/></svg></div>
</footer>

</body>
</html>
```